New landing page

We have an existing design at www.hostqubit.com but we are not set on that design and probably want something different.
We want to increase conversion rates and experiment with a new landing page for our lumo bidclick campains.
We want to use a more single page long design page that contains these elements on one page:

Header
Images/headline
4 offer boxes
Features
Locations (map)
Testimonials
Why HostQubit
Footer menu

Note should also be taken of research done by Fernlatch like this:
http://fernlatch.com/landing-page-articles/the-anatomy-of-a-landing-page/

```html
<!DOCTYPE html>
<html lang="en">
<head>
<meta charset="utf-8">
<title>HostQubit – Your own Linux Server in 59 seconds</title>
<link rel="stylesheet" href="https://fonts.googleapis.com/css2?family=Open+Sans:ital,wght@0,400;0,600;0,700;1,400&display=swap">
<style>
:root{
  --ink:#2b2b2b;
  --muted:#8a8a8a;
  --dark:#232323;
  --footer:#1d1d1d;
  --yellow:#f6b203;
  --yellow-dark:#c98f00;
  --gold:#e4a20e;
  --rust:#cf4a1c;
  --tag:#c8401a;
  --navy:#14293a;
  --pale:#f5f5f7;
  --line:#d5d5d5;
  --white:#ffffff;
}
*{box-sizing:border-box;margin:0;padding:0}
html,body{width:1200px;height:3130px;overflow:hidden}
body{font-family:"Open Sans",Arial,sans-serif;color:var(--ink);background:var(--white);position:relative}
section,header,nav,footer{position:absolute;left:0;width:1200px}

/* header */
.topbar{top:0;height:100px;background:var(--dark);color:#ddd;font-size:17px}
.brand{position:absolute;left:100px;top:25px;display:flex;align-items:center;gap:14px}
.brand-dot{width:46px;height:46px;border-radius:50%;background:var(--yellow)}
.brand-name{font-size:42px;font-weight:600;color:var(--white);letter-spacing:-1px}
.contact{position:absolute;top:38px;display:flex;align-items:center;gap:10px}
.contact svg{fill:#bbb}
.c-phone{left:522px}.c-mail{left:730px}.c-account{left:980px}

.mainnav{top:100px;height:52px;background:var(--yellow)}
.mainnav ul{list-style:none;display:flex;height:52px;margin-left:100px}
.mainnav li{font-size:14px;font-weight:600;color:#3a2a00;line-height:52px;padding:0 21.5px}
.mainnav li.active{background:var(--yellow-dark);color:var(--white)}

/* hero */
.hero{top:152px;height:328px;background:linear-gradient(#e6e6e8,#dcdcde)}
.hero h1{position:absolute;left:100px;top:64px;font-weight:400;font-size:40px;line-height:44px;color:#333}
.hero p{position:absolute;left:102px;top:160px;width:480px;font-size:13.5px;line-height:21px;color:#555}
.hero-visual{position:absolute;left:640px;top:22px;width:480px;height:250px;border-radius:6px;
  background:linear-gradient(135deg,#f4f4f4 0%,#bdbdc0 60%,#8d8d90 100%)}
.slide-arrow{position:absolute;top:148px}
.slide-arrow.left{left:28px}.slide-arrow.right{right:28px}

/* pricing */
.pricing{top:480px;height:448px;background:var(--white)}
.plan{position:absolute;top:46px;width:192px;text-align:center}
.plan h2{font-size:19px;font-weight:400;color:var(--rust);height:37px}
.plan-card{background:linear-gradient(#f3f3f3,#e8e8e8);border:1px solid #d6d6d6;height:251px;position:relative}
.price-tag{position:absolute;left:36px;top:0;width:120px;height:67px;background:var(--tag);color:var(--white);
  clip-path:polygon(0 0,100% 0,100% 100%,50% 84%,0 100%)}
.price-tag b{display:block;font-size:28px;font-weight:400;line-height:32px;margin-top:4px}
.price-tag i{display:block;font-size:11px;color:#f7c8b4}
.plan-specs{list-style:none;position:absolute;top:94px;left:12px;right:12px}
.plan-specs li{font-size:11px;color:#555;height:29.5px;line-height:28px;border-bottom:1px dashed #c8c8c8}
.plan-specs li:last-child{border-bottom:none}
.order{display:block;height:52px;line-height:52px;background:var(--navy);color:var(--white);font-size:23px;font-weight:400}

/* features */
.features{top:928px;height:783px;background:var(--pale)}
.section-title{font-size:29px;font-weight:600;color:var(--gold);text-align:center}
.features .section-title{margin-top:38px}
.feature{position:absolute;width:420px;padding-left:46px}
.feature svg{position:absolute;left:0;top:2px}
.feature h3{font-size:20px;font-weight:600;color:#333;line-height:24px}
.feature p{font-size:13.5px;color:#999;line-height:21px;margin-top:4px}
.col-l{left:136px}.col-r{left:670px}

/* why */
.why{top:1711px;height:501px;background:var(--white);text-align:center}
.why .section-title{margin-top:56px}
.why-copy{width:880px;margin:24px auto 0;font-size:14.5px;line-height:21px;color:#777}
.why-list{list-style:none;margin-top:24px}
.why-list li{font-size:19px;color:#333;line-height:38.5px}
.why-list li::before{content:"\2713";font-size:15px;margin-right:8px;color:#444}

/* testimonials */
.testimonials{top:2212px;height:282px;background:var(--pale)}
.testimonials .section-title{margin-top:48px}
.avatar{position:absolute;left:130px;top:100px;width:126px;height:126px;border-radius:50%;
  border:5px solid var(--white);box-shadow:0 2px 8px rgba(0,0,0,.2);
  background:radial-gradient(circle at 50% 40%,#e8cbb6,#c69f86 60%,#d9d9d9)}
.quote{position:absolute;left:272px;top:112px;width:810px;font-size:14px;font-style:italic;line-height:24px;color:#888}
.quote-name{position:absolute;left:272px;top:194px;font-size:15px;color:#b52a1c}
.testimonials .slide-arrow{top:136px}

/* partners */
.partners{top:2494px;height:131px;background:var(--white);display:flex;align-items:center;justify-content:center;gap:46px}
.badge{height:44px;background:#d9d9d9;border-radius:6px}

/* map */
.map{top:2625px;height:297px;background:linear-gradient(160deg,#dcdcdc,#c9c9c9 55%,#d4d4d4)}

/* footer */
.site-footer{top:2922px;height:208px;background:var(--footer);text-align:center;color:#9a9a9a}
.footer-links{list-style:none;display:flex;justify-content:center;margin-top:48px;font-size:13.5px}
.footer-links li+li::before{content:"/";margin:0 12px;color:#666}
.copyright{font-size:13.5px;margin-top:16px}
.social{display:flex;justify-content:center;gap:16px;margin-top:28px}
.social span{width:34px;height:34px;border-radius:4px;background:#5a5a5a}
</style>
</head>
<body>

<header class="topbar">
  <div class="brand"><span class="brand-dot"></span><span class="brand-name">HostQubit</span></div>
  <div class="contact c-phone">
    <svg width="20" height="18" viewBox="0 0 20 18"><path d="M3 4c0-2 2-3 4-3h6c2 0 4 1 4 3v2h-4V4H7v2H3zM4 8h12l2 9H2z"/></svg>
    <span>+1 800 555 0147</span>
  </div>
  <div class="contact c-mail">
    <svg width="22" height="16" viewBox="0 0 22 16"><path d="M0 0h22v16H0z M2 2l9 7 9-7" stroke="#232323" stroke-width="1.5"/></svg>
    <span>support@hostqubit.com</span>
  </div>
  <div class="contact c-account">
    <svg width="18" height="18" viewBox="0 0 18 18"><circle cx="9" cy="5" r="4.5"/><path d="M0 18c0-6 4-8 9-8s9 2 9 8z"/></svg>
    <span>My Account</span>
  </div>
</header>

<nav class="mainnav">
  <ul>
    <li class="active">HOME</li><li>SERVICES</li><li>FEATURES</li><li>LOCATIONS</li><li>FAQ</li>
    <li>PAYMENT METHODS</li><li>COMMUNITY</li><li>SUPPORT</li><li>ABOUT</li>
  </ul>
</nav>

<section class="hero">
  <svg class="slide-arrow left" width="16" height="28" viewBox="0 0 16 28"><path d="M14 2 3 14l11 12" fill="none" stroke="#666" stroke-width="3"/></svg>
  <h1>Your own<br>Linux Server in 59 seconds</h1>
  <p>With 24x7x365 support, instant setup and upgrades, 99% uptime and our 14 day no questions asked money back gurantee, servers in New Zealand,Singapore,Hong Kong, Switzerland,Germany,South Africa and New York City... plus our great pricing, why would you look anywhere else?</p>
  <div class="hero-visual" role="img" aria-label="Silver rack-mounted server unit"></div>
  <svg class="slide-arrow right" width="16" height="28" viewBox="0 0 16 28"><path d="M2 2l11 12L2 26" fill="none" stroke="#666" stroke-width="3"/></svg>
</section>

<section class="pricing">
  <div class="plan" style="left:198px">
    <h2>BUDGET VPS</h2>
    <div class="plan-card">
      <div class="price-tag"><b>$10</b><i>per month</i></div>
      <ul class="plan-specs"><li>256 MB Guaranteed RAM</li><li>1x 3.4 Ghz Cores</li><li>10 GB Raid-10 Storage</li><li>300 GB Bandwidth</li><li>59 second Activation</li></ul>
    </div>
    <a class="order">ORDER NOW</a>
  </div>
  <div class="plan" style="left:401px">
    <h2>STANDARD VPS</h2>
    <div class="plan-card">
      <div class="price-tag"><b>$25</b><i>per month</i></div>
      <ul class="plan-specs"><li>256 MB Guaranteed RAM</li><li>1x 3.4 Ghz Cores</li><li>10 GB Raid-10 Storage</li><li>300 GB Bandwidth</li><li>59 second Activation</li></ul>
    </div>
    <a class="order">ORDER NOW</a>
  </div>
  <div class="plan" style="left:604px">
    <h2>EXTREME VPS</h2>
    <div class="plan-card">
      <div class="price-tag"><b>$40</b><i>per month</i></div>
      <ul class="plan-specs"><li>256 MB Guaranteed RAM</li><li>1x 3.4 Ghz Cores</li><li>10 GB Raid-10 Storage</li><li>300 GB Bandwidth</li><li>59 second Activation</li></ul>
    </div>
    <a class="order">ORDER NOW</a>
  </div>
  <div class="plan" style="left:807px">
    <h2>CUSTOM VPS</h2>
    <div class="plan-card">
      <div class="price-tag"><b>$10</b><i>per month</i></div>
      <ul class="plan-specs"><li>256 MB Guaranteed RAM</li><li>1x 3.4 Ghz Cores</li><li>10 GB Raid-10 Storage</li><li>300 GB Bandwidth</li><li>59 second Activation</li></ul>
    </div>
    <a class="order">ORDER NOW</a>
  </div>
</section>

<section class="features">
  <h2 class="section-title">VIP Hosting Features</h2>

  <div class="feature col-l" style="top:133px">
    <svg width="30" height="30" viewBox="0 0 30 30"><circle cx="15" cy="15" r="12" fill="none" stroke="#444" stroke-width="2.5"/><path d="M15 8v7h6" fill="none" stroke="#444" stroke-width="2.5"/></svg>
    <h3>59 Second Activation</h3><p>Your virtual host will be activated immediately after<br>your first payment, so you dont wait.</p>
  </div>
  <div class="feature col-r" style="top:133px">
    <svg width="30" height="30" viewBox="0 0 30 30" fill="none" stroke="#444" stroke-width="2.5"><path d="M3 11a17 17 0 0 1 24 0M7 15a11 11 0 0 1 16 0M11 19a5 5 0 0 1 8 0"/><circle cx="15" cy="23" r="1.5" fill="#444"/></svg>
    <h3>99.9% Uptime</h3><p>Your virtual host will be activated immediately after<br>your first payment, so you dont wait.</p>
  </div>

  <div class="feature col-l" style="top:261px">
    <svg width="30" height="30" viewBox="0 0 30 30"><rect x="2" y="9" width="26" height="13" fill="#888"/><rect x="5" y="12" width="6" height="7" fill="#ccc"/></svg>
    <h3>14 Day Moneyback Guarantee</h3><p>Your virtual host will be activated immediately after<br>your first payment, so you dont wait.</p>
  </div>
  <div class="feature col-r" style="top:261px">
    <svg width="30" height="30" viewBox="0 0 30 30"><rect x="6" y="3" width="18" height="24" rx="2" fill="none" stroke="#444" stroke-width="2.5"/><circle cx="15" cy="13" r="4" fill="#444"/></svg>
    <h3>Full Root Access</h3><p>Your virtual host will be activated immediately after<br>your first payment, so you dont wait.</p>
  </div>

  <div class="feature col-l" style="top:390px">
    <svg width="30" height="30" viewBox="0 0 30 30"><circle cx="15" cy="15" r="12" fill="none" stroke="#444" stroke-width="6" stroke-dasharray="9 9.8"/><circle cx="15" cy="15" r="12" fill="none" stroke="#444" stroke-width="1.5"/></svg>
    <h3>24/7/365 Support</h3><p>Your virtual host will be activated immediately after<br>your first payment, so you dont wait.</p>
  </div>
  <div class="feature col-r" style="top:390px">
    <svg width="30" height="30" viewBox="0 0 30 30" fill="none" stroke="#444" stroke-width="2.2"><circle cx="15" cy="15" r="12"/><ellipse cx="15" cy="15" rx="5" ry="12"/><path d="M3 15h24"/></svg>
    <h3>Global Locations</h3><p>Your virtual host will be activated immediately after<br>your first payment, so you dont wait.</p>
  </div>

  <div class="feature col-l" style="top:518px">
    <svg width="30" height="30" viewBox="0 0 30 30"><rect x="1" y="4" width="28" height="18" fill="#222"/><rect x="4" y="7" width="22" height="12" fill="#fff"/><rect x="11" y="22" width="8" height="4" fill="#222"/><rect x="7" y="26" width="16" height="2" fill="#222"/></svg>
    <h3>Choice of operating systems</h3><p>Your virtual host will be activated immediately after<br>your first payment, so you dont wait.</p>
  </div>
  <div class="feature col-r" style="top:518px">
    <svg width="30" height="30" viewBox="0 0 30 30" stroke="#444" stroke-width="3" fill="none"><path d="M5 5l20 20M25 5 5 25"/></svg>
    <h3>PanelDeck/Rootboard</h3><p>Your virtual host will be activated immediately after<br>your first payment, so you dont wait.</p>
  </div>

  <div class="feature col-l" style="top:647px">
    <svg width="30" height="30" viewBox="0 0 30 30"><rect x="2" y="10" width="26" height="11" fill="none" stroke="#666" stroke-width="2"/><path d="M6 15.5h18" stroke="#999" stroke-width="2"/></svg>
    <h3>IP Adresses</h3><p>Your virtual host will be activated immediately after<br>your first payment, so you dont wait.</p>
  </div>
  <div class="feature col-r" style="top:647px">
    <svg width="30" height="30" viewBox="0 0 30 30" fill="none" stroke="#444" stroke-width="3"><path d="M18 26V10H8M13 5 8 10l5 5"/></svg>
    <h3>Upgrades with no downtime</h3><p>Your virtual host will be activated immediately after<br>your first payment, so you dont wait.</p>
  </div>
</section>

<section class="why">
  <h2 class="section-title">Why HostQubit</h2>
  <p class="why-copy">Nam eleifend vitae erat in tempus. In suscipit metus in congue vehicula. Integer mollis, lectus vel hendrerit ullamcorper, tortor augue feugiat lectus, nec viverra leo nunc eleifend libero. Proin porta est vitae tristique bibendum. Curabitur accum san lacus ac pharetra porta. Sed mattis, turpis faucibus cursus ullamcorper, ipsum magna dignissim libero, eu dictum risus nibh eu turpis. Duis sit amet faucibus ante.</p>
  <ul class="why-list">
    <li>Donec tempus porta tempus</li>
    <li>Suspendisse iaculis ligula ac lacus eleifend</li>
    <li>Aenean at lorem a risus viverra feugiat id sit amet</li>
    <li>Aliquam dictum felis vel metus</li>
    <li>liquam adipiscing iaculis eros vel placerat.</li>
  </ul>
</section>

<section class="testimonials">
  <h2 class="section-title">Testimonials</h2>
  <svg class="slide-arrow left" width="16" height="28" viewBox="0 0 16 28"><path d="M14 2 3 14l11 12" fill="none" stroke="#aaa" stroke-width="3"/></svg>
  <div class="avatar" role="img" aria-label="Portrait photo of the customer"></div>
  <p class="quote">“ Nam a malesuada libero. Duis sodales et libero vel interdum. Interdum et malesuada fames ac ante ipsum primis in faucibus. Donec lobortis dui tortor, eu lobortis felis mattis nec. Sed justo quam, luctus eu mauris eget, euismod dapibus sem. Sed tempus feugiat ante, at ornare libero volutpat sed. Maecenas quis magna magna. ”</p>
  <p class="quote-name">Daren - Team Name</p>
  <svg class="slide-arrow right" width="16" height="28" viewBox="0 0 16 28"><path d="M2 2l11 12L2 26" fill="none" stroke="#aaa" stroke-width="3"/></svg>
</section>

<section class="partners">
  <span class="badge" style="width:96px"></span>
  <span class="badge" style="width:88px"></span>
  <span class="badge" style="width:120px"></span>
  <span class="badge" style="width:114px"></span>
  <span class="badge" style="width:84px"></span>
  <span class="badge" style="width:104px"></span>
  <span class="badge" style="width:110px"></span>
</section>

<section class="map" role="img" aria-label="Greyscale street map showing the data centre location"></section>

<footer class="site-footer">
  <ul class="footer-links">
    <li>Home</li><li>Services</li><li>Features</li><li>Locations</li><li>FAQ</li><li>Payment Methods</li><li>Community</li><li>Support</li><li>About</li><li>Sitemap</li>
  </ul>
  <p class="copyright">Copyright © 2014 HostQubit. All rights reserved.</p>
  <div class="social"><span></span><span></span><span></span></div>
</footer>

</body>
</html>
```